OTV Web Design Project

I'm looking for a small, friendly,functional, information based website. If you go through the attachments, you would know the nature of the business.
Updates

Hi,

I have uploaded a picture of the CEO, Mr. Darvesh Kolhi NAMPQ member. Please feel free to use it whereever appropriate.

Thanks!

Hello, I have uploaded some references. I like the colours used on the bar and would w

Example of a we page . I like this layout for the inside pages.

I am changing the tabs on my website to:

Home
About us
Services
Contact us

The services tab will have three sub pages:

Immigration
Education
AccommodationAccommodation

Target Market(s)

Young international students willing to come to Canada to study, young international students willing to immigrate to Canada, parents of the students

Industry/Entity Type

Business

Requirements
Must have
• OTV HOME
ABOUT US
CONTACT
SERVICES
TAG LINE

The website should look n feel trendy, smart, current, factual, trustworthy etc....
Nice to have
• I am looking for a bold, attractive, eye catchy home page with less text! Something that makes a statement....
Should not have
• No Clip art, flash animation, no bells n whistles please

```html
<!DOCTYPE html>
<html lang="en">
<head>
<meta charset="utf-8">
<title>OTV – Orion Trail Ventures</title>
<link rel="stylesheet" href="https://fonts.googleapis.com/css2?family=Archivo+Black&family=Montserrat:wght@500;700&family=Open+Sans:wght@400&family=Ubuntu:wght@400;500;700&display=swap">
<style>
  :root{
    --red:#ed1c24;
    --dot:#8a1a12;
    --ink:#2b2b2b;
    --grey:#6d6e71;
    --page-bg:#e6e6e7;
    --panel-bg:#f3f4f5;
    --brown:#5a4422;
    --footer-ink:#3f4448;
    --badge:#c9cbce;
    --white:#ffffff;
  }
  *{box-sizing:border-box;margin:0;padding:0}
  html,body{width:1200px;height:1153px;overflow:hidden;background:var(--white)}
  .canvas{position:relative;width:1200px;height:1153px;overflow:hidden;
    background:radial-gradient(ellipse at 50% 30%, #f7f7f7 0%, var(--page-bg) 70%, #d9d9da 100%);
    font-family:"Open Sans",Verdana,sans-serif;color:var(--ink)}
  .top-rule{position:absolute;left:0;top:0;width:1200px;height:5px;background:var(--red)}

  /* header */
  .brand{position:absolute;left:136px;top:40px}
  .brand-mark{display:flex;align-items:center;gap:10px}
  .brand-mark .acronym{font-family:"Ubuntu",sans-serif;font-weight:700;font-size:54px;color:#262626;line-height:1;letter-spacing:1px}
  .brand-mark .square{width:26px;height:26px;background:var(--red)}
  .brand-name{font-family:"Ubuntu",sans-serif;font-weight:500;font-size:27px;color:var(--grey);margin-top:6px;line-height:1}
  .brand-tagline{font-family:"Ubuntu",sans-serif;font-style:italic;font-size:11px;color:#333;margin:4px 0 0 92px}

  .social{position:absolute;top:11px;left:873px;display:flex;gap:10px}
  .social span{width:28px;height:28px;border-radius:5px;background:linear-gradient(#6c8fc7,#3b5d99)}
  .social span:nth-child(2){background:linear-gradient(#8fd3f2,#3aa6d8)}
  .social span:nth-child(3){background:linear-gradient(#4d9fd0,#1b6aa0)}
  .social span:nth-child(4){background:linear-gradient(#e35b48,#c0321f)}
  .social span:nth-child(5){background:linear-gradient(#e2474f,#b91c23)}

  .contact-line{position:absolute;right:151px;display:flex;align-items:center;gap:8px;font-family:"Montserrat",sans-serif;font-weight:500;color:var(--brown)}
  .contact-line.phone{top:96px;font-size:25px;letter-spacing:1px}
  .contact-line.email{top:138px;font-size:19px;color:#3d2e18}

  /* column */
  .column{position:absolute;left:136px;top:172px;width:928px;height:868px;background:var(--white)}
  .nav{height:34px;background:var(--red);display:flex;align-items:center;padding-left:23px;gap:24px}
  .nav a{font-family:"Montserrat",sans-serif;font-weight:700;font-size:13.5px;color:var(--white);text-decoration:none;letter-spacing:.3px}

  .hero{position:relative;height:419px;overflow:hidden}
  .hero-photo{position:absolute;inset:0;background:
      linear-gradient(100deg, rgba(88,110,125,0) 0%, rgba(88,110,125,0) 55%, rgba(196,120,90,.35) 75%, rgba(220,90,80,.35) 100%),
      linear-gradient(180deg,#7ea3d6 0%,#9dbbe1 35%,#8a8580 60%,#6e6a55 85%,#5d6b4a 100%)}
  .hero-title{position:absolute;font-family:"Archivo Black",sans-serif;font-size:41px;color:var(--red);line-height:1;
    text-shadow:-2px -2px 0 #fff,2px -2px 0 #fff,-2px 2px 0 #fff,2px 2px 0 #fff,0 2px 0 #fff,0 -2px 0 #fff,2px 0 0 #fff,-2px 0 0 #fff}
  .hero-title.l1{left:15px;top:12px}
  .hero-title.l2{left:150px;top:61px}
  .hero-title.l3{left:239px;top:109px}
  .hero-arrow{position:absolute;top:166px;width:28px;height:28px}
  .hero-arrow.prev{left:10px}
  .hero-arrow.next{right:10px}
  .hero-curve{position:absolute;left:0;bottom:0;width:928px;height:90px}
  .slider-dots{position:absolute;left:38px;top:434px;display:flex;gap:10px}
  .slider-dots span{width:11px;height:11px;border-radius:3px;background:var(--dot)}
  .slider-dots span.active{background:var(--red);box-shadow:0 0 0 2px #f6c6c6}

  /* info panels */
  .panel{position:absolute;top:503px;width:279px;height:245px;background:var(--panel-bg);border:1px solid #d6d7d8;border-radius:3px;
    box-shadow:0 1px 2px rgba(0,0,0,.12);overflow:hidden}
  .panel.welcome{left:23px}
  .panel.services{left:322px}
  .panel.reviews{left:625px}
  .panel-head{height:37px;background:var(--red);display:flex;align-items:center;gap:10px;padding-left:24px;
    font-family:"Ubuntu",sans-serif;font-weight:400;font-size:19px;color:var(--white);letter-spacing:.3px}
  .panel-head svg{flex:none}
  .panel-body{padding:13px 26px 0 26px;font-size:11.5px;line-height:16.3px;color:#2e2e2e;letter-spacing:.2px}
  .learn-more{position:absolute;bottom:14px;right:30px;display:flex;align-items:center;gap:4px;font-size:10px;color:var(--red);text-decoration:none}

  .service-list{list-style:none;padding:16px 0 0 12px}
  .service-list li{display:flex;align-items:flex-start;gap:12px;font-family:"Ubuntu",sans-serif;font-size:17.5px;color:#1e1e1e;line-height:20px;margin-bottom:29px}
  .service-list li::before{content:"";flex:none;width:12px;height:12px;margin-top:4px;background:var(--red)}

  .quote-mark{position:absolute;left:6px;top:42px;font-family:"Archivo Black",sans-serif;font-size:46px;color:#c9c9c9;line-height:1}
  .reviews .panel-body{padding:14px 16px 0 28px}
  .reviewer{position:absolute;right:16px;bottom:8px;display:flex;align-items:center;gap:9px;text-align:right;font-size:12px;line-height:16px;color:var(--red)}
  .reviewer-photo{width:64px;height:51px;border:1px solid #c9c9c9;background:linear-gradient(135deg,#d9dde2,#b9a494)}

  .swoosh{position:absolute;left:0;bottom:0;width:928px;height:98px}

  /* footer */
  .copyright{position:absolute;left:159px;top:1075px;font-size:10px;line-height:15.5px;color:#7a7a7a}
  .council{position:absolute;left:652px;top:1060px;display:flex;flex-direction:column}
  .council .abbr{font-family:"Ubuntu",sans-serif;font-weight:500;font-size:40px;line-height:1;color:var(--footer-ink);letter-spacing:2px}
  .council .full{font-family:"Ubuntu",sans-serif;font-weight:500;font-size:8px;line-height:11px;color:var(--footer-ink);margin-top:8px;text-transform:uppercase}
  .council-badge{position:absolute;left:900px;top:1058px;width:160px;height:66px;border-radius:6px;background:var(--badge)}
</style>
</head>
<body>
<div class="canvas">
  <div class="top-rule"></div>

  <header>
    <div class="brand">
      <div class="brand-mark"><span class="acronym">OTV</span><span class="square"></span></div>
      <div class="brand-name">Orion Trail Ventures</div>
      <div class="brand-tagline">Taking you onwards.....</div>
    </div>

    <div class="social" aria-label="Social links"><span></span><span></span><span></span><span></span><span></span></div>

    <div class="contact-line phone">
      <svg width="18" height="14" viewBox="0 0 18 14" aria-hidden="true"><path d="M1 4c0-2 3-3 8-3s8 1 8 3v1h-4V4H5v1H1z" fill="#333"/><rect x="3" y="6" width="12" height="7" rx="1" fill="#333"/><circle cx="9" cy="9.5" r="2" fill="#ddd"/></svg>
      <span>(555) 014 2277</span>
    </div>
    <div class="contact-line email">
      <svg width="24" height="18" viewBox="0 0 24 18" aria-hidden="true"><rect x="1" y="3" width="20" height="13" rx="1" fill="#e9efe4" stroke="#9aa88f"/><path d="M1 3l10 8 10-8" fill="none" stroke="#9aa88f"/><circle cx="8" cy="7" r="5" fill="#6fb442"/></svg>
      <span>info@oriontrailventures.com</span>
    </div>
  </header>

  <main class="column">
    <nav class="nav">
      <a href="#">HOME</a><a href="#">ABOUT US</a><a href="#">SERVICES</a><a href="#">CONTACT</a><a href="#">OTV MISSION</a>
    </nav>

    <section class="hero">
      <div class="hero-photo" role="img" aria-label="Group of smiling international students in front of a historic stone university building"></div>
      <h1>
        <span class="hero-title l1">DARE TO</span>
        <span class="hero-title l2">DREAM</span>
        <span class="hero-title l3">CANADIAN...</span>
      </h1>
      <svg class="hero-arrow prev" viewBox="0 0 28 28" aria-hidden="true"><circle cx="14" cy="14" r="13" fill="rgba(255,255,255,.55)"/><path d="M16 8l-6 6 6 6M10 14h10" stroke="#8a9bb0" stroke-width="3" fill="none"/></svg>
      <svg class="hero-arrow next" viewBox="0 0 28 28" aria-hidden="true"><circle cx="14" cy="14" r="13" fill="rgba(255,255,255,.55)"/><path d="M12 8l6 6-6 6M18 14H8" stroke="#8a9bb0" stroke-width="3" fill="none"/></svg>
      <svg class="hero-curve" viewBox="0 0 928 90" preserveAspectRatio="none" aria-hidden="true">
        <path d="M0 16 C 260 70, 600 86, 928 56 L928 90 L0 90Z" fill="var(--red)"/>
        <path d="M0 26 C 250 78, 600 94, 928 64 L928 90 L0 90Z" fill="#fff"/>
      </svg>
    </section>

    <div class="slider-dots"><span class="active"></span><span></span><span></span><span></span></div>

    <article class="panel welcome">
      <h2 class="panel-head">
        <svg width="32" height="32" viewBox="0 0 32 32" aria-hidden="true"><circle cx="16" cy="16" r="15" fill="#fff"/><circle cx="16" cy="9" r="2.6" fill="var(--red)"/><rect x="13.5" y="13" width="5" height="12" fill="var(--red)"/></svg>
        WELCOME TO OTV
      </h2>
      <p class="panel-body">Darvesh Kolhi, CEO of Orion Trail Ventures, has vast knowledge in the field of Student Recruitment &amp; Higher Education. He is an MBA from Canada and is very well known in the India-Canada education corridor since 2004. He has served as India, Africa &amp; Middle East Head for Lakeshore College in the past, in addition to providing consultant services for various elite</p>
      <a class="learn-more" href="#">Learn more <svg width="11" height="9" viewBox="0 0 11 9" aria-hidden="true"><path d="M0 3h5V0l6 4.5L5 9V6H0z" fill="var(--red)"/></svg></a>
    </article>

    <article class="panel services">
      <h2 class="panel-head">
        <svg width="28" height="32" viewBox="0 0 28 32" aria-hidden="true"><rect x="3" y="4" width="20" height="26" fill="#fff" stroke="#999" transform="rotate(-8 13 17)"/><path d="M9 14h10M9 18h10M9 22h7" stroke="#aaa" transform="rotate(-8 13 17)"/><path d="M22 2l4 3-10 14-4 1 1-4z" fill="#555"/></svg>
        OTV SERVICES
      </h2>
      <ul class="service-list">
        <li>IMMIGRATION SERVICES</li>
        <li>EDUCATION SERVICES</li>
        <li>STUDENT ACCOMODATION<br>SERVICES</li>
      </ul>
      <a class="learn-more" href="#">Learn more <svg width="11" height="9" viewBox="0 0 11 9" aria-hidden="true"><path d="M0 3h5V0l6 4.5L5 9V6H0z" fill="var(--red)"/></svg></a>
    </article>

    <article class="panel reviews">
      <h2 class="panel-head" style="padding-left:12px">
        <svg width="36" height="26" viewBox="0 0 36 26" aria-hidden="true"><ellipse cx="13" cy="10" rx="12" ry="8.5" fill="#fff"/><path d="M6 16l-3 7 8-5z" fill="#fff"/><ellipse cx="24" cy="14" rx="11" ry="8" fill="#fff" stroke="var(--red)" stroke-width="1.5"/><path d="M28 21l4 4-1-6z" fill="#fff"/></svg>
        WHAT STUDENTS SAY!!
      </h2>
      <span class="quote-mark" aria-hidden="true">“</span>
      <p class="panel-body">Lorem Ipsum. Proin gravida nibh vel veli auctor aliquet. Aenean sollicitudin, lorem quis bibendum auctor, nisi elit consetop qua ipsum, nec sagittis sem nibh id elit. Duis sed odio sit amet nibh vulputateai cursus a sit amet mauris. Morbi jwrtdrao accumsan ipsum velit. Nam nec tellus as odio tincidunt auctor a ornare odio...</p>
      <div class="reviewer">
        <span>Melissa<br>South Africa</span>
        <div class="reviewer-photo" role="img" aria-label="Portrait photo of the student"></div>
      </div>
    </article>

    <svg class="swoosh" viewBox="0 0 928 98" preserveAspectRatio="none" aria-hidden="true">
      <defs>
        <linearGradient id="swooshFill" x1="0" y1="0" x2="0" y2="1">
          <stop offset="0" stop-color="#a9aaac"/><stop offset="1" stop-color="#8d8e90"/>
        </linearGradient>
      </defs>
      <path d="M0 0 C 220 40, 520 70, 928 0 L928 98 L0 98Z" fill="url(#swooshFill)"/>
      <path d="M0 0 C 240 48, 560 64, 928 6" fill="none" stroke="#d7d8d9" stroke-width="3"/>
      <path d="M0 12 C 260 58, 580 70, 928 16" fill="none" stroke="#c4c5c7" stroke-width="1.5"/>
    </svg>
  </main>

  <footer>
    <p class="copyright">Copy (c) 2013. Orion Trail Ventures,<br>All Rights Reserved.</p>
    <div class="council"><span class="abbr">NAMPQ</span><span class="full">National Association of<br>Migration Practice Qualifiers</span></div>
    <div class="council-badge" role="img" aria-label="Partner council badge"></div>
  </footer>
</div>
</body>
</html>
```